Wine label for premium wine of vinery Vrbolanec.

Design Premium wine label.

The brand is called Melvara. Brand can be extended to Dorano Melvara. There
The label should be unique and high class feeling.
This is facebook lonk of the winery
https://www.pagebook.example/402918365510274/

On facebook you can see some examole of labels that are used now. Winery is called Vrbolanec, so they used letter "K" as a logo in different ways

Target Market(s)

Premium high class yet modern living traditional but also gadget fun.
I have uploaded few inspirational photos that the owner of the vinery likes. Hope it helps.

Industry/Entity Type

Vinery

Requirements
Must have
• Black, gold, silver color to be dominated. Colors that are NOT acceptable are: green, yellow, blue, purple, pink.

The name of the vinary is Vrbolanec and it should be on the front label.
Nice to have
• The size of label should fit the Grapely application screenshot frame.
Should not have
• Cheap perception of the label and brand

```html
<!DOCTYPE html>
<html lang="en">
<head>
<meta charset="utf-8">
<title>Melvara Sauvignon Blanc – Vrbolanec front label</title>
<link rel="stylesheet" href="https://fonts.googleapis.com/css2?family=Crimson+Pro:wght@400;500&family=Mrs+Saint+Delafield&display=swap">
<style>
  :root {
    --page: #ffffff;
    --slate-dark: #2a2a2a;
    --slate-mid: #4a4a4a;
    --slate-light: #6b6b6b;
    --paper: #f7f7f6;
    --paper-shade: #e6e6e4;
    --sketch: #d4d4d2;
    --ink: #2b2b2b;
    --silver: #f1f1f1;
    --gold: #b59a62;
    --gold-light: #d8c28f;
    --seal: #1e1e1e;
    --seal-ring: #8d7a52;
    --region-red: #8a1c1c;
  }
  * { margin: 0; padding: 0; box-sizing: border-box; }
  html, body {
    width: 1016px; height: 1200px; overflow: hidden;
    background: var(--page);
  }
  .label {
    position: absolute; left: 98px; top: 40px;
    width: 820px; height: 1120px;
    background: var(--paper);
    overflow: hidden;
    box-shadow: 0 2px 14px rgba(0,0,0,0.12);
  }
  .label__band {
    position: absolute; inset: 0 0 auto 0; height: 660px;
    background: linear-gradient(100deg, var(--slate-dark) 0%, var(--slate-mid) 35%, var(--slate-light) 55%, var(--slate-mid) 75%, var(--slate-dark) 100%);
  }
  .label__tear { position: absolute; left: 0; top: 610px; width: 820px; height: 90px; }
  .winery-name {
    position: absolute; top: 100px; left: 0; width: 100%;
    text-align: center;
    font-family: "Crimson Pro", serif; font-weight: 500;
    font-size: 42px; letter-spacing: 0.16em;
    color: var(--silver);
  }
  .region-mark {
    position: absolute; left: 528px; top: 176px; width: 38px; height: 28px;
    border-radius: 45% 55% 50% 40%;
    background: var(--region-red);
    transform: rotate(20deg);
  }
  .wine-name {
    position: absolute; top: 290px; left: 0; width: 100%;
    text-align: center;
    font-family: "Mrs Saint Delafield", cursive;
    font-size: 190px; line-height: 1;
    color: var(--gold);
    background: linear-gradient(90deg, var(--gold) 0%, var(--gold-light) 45%, var(--gold) 100%);
    -webkit-background-clip: text; background-clip: text;
    -webkit-text-fill-color: transparent;
  }
  .seal {
    position: absolute; left: 305px; top: 522px; width: 210px; height: 210px;
    border-radius: 50%;
    background: radial-gradient(circle at 40% 35%, #3a3a3a 0%, var(--seal) 70%);
    border: 3px solid var(--seal-ring);
    box-shadow: 0 6px 14px rgba(0,0,0,0.35);
  }
  .seal-name {
    position: absolute; left: 528px; top: 612px;
    font-family: "Crimson Pro", serif; font-weight: 500;
    font-size: 24px; letter-spacing: 0.12em;
    color: var(--silver);
  }
  .vineyard-scene {
    position: absolute; left: 0; top: 700px; width: 100%; height: 330px;
    background: radial-gradient(ellipse at 50% 40%, var(--paper-shade) 0%, var(--paper) 75%);
  }
  .varietal {
    position: absolute; left: 0; top: 935px; width: 100%;
    text-align: center;
    font-family: "Crimson Pro", serif; font-weight: 400;
    font-size: 48px; color: var(--ink);
  }
  .rule {
    position: absolute; left: 224px; top: 1012px; width: 372px; height: 3px;
    background: var(--gold);
  }
  .origin {
    position: absolute; left: 0; top: 1022px; width: 100%;
    text-align: center;
    font-family: "Crimson Pro", serif; font-weight: 400;
    font-size: 48px; color: var(--ink);
  }
</style>
</head>
<body>
  <main class="label">
    <div class="label__band"></div>
    <svg class="label__tear" viewBox="0 0 820 90" preserveAspectRatio="none" aria-hidden="true">
      <path d="M0 48 L40 40 L70 44 L95 30 L130 36 L160 22 L200 30 L230 26 L270 38 L300 30 L330 34 L360 28 L400 40 L440 30 L480 36 L520 28 L560 34 L600 24 L640 32 L680 26 L720 44 L760 38 L790 46 L820 40 L820 90 L0 90 Z" fill="#ffffff"/>
      <path d="M0 56 L40 48 L70 52 L95 40 L130 44 L160 32 L200 40 L230 36 L270 46 L300 40 L330 42 L360 36 L400 48 L440 40 L480 44 L520 36 L560 42 L600 34 L640 40 L680 36 L720 52 L760 46 L790 54 L820 48 L820 90 L0 90 Z" fill="var(--paper)"/>
    </svg>

    <h1 class="winery-name">VRBOLANEC</h1>
    <div class="region-mark" role="img" aria-label="Small red map of the winery's home region"></div>
    <p class="wine-name">Melvara</p>

    <div class="vineyard-scene" role="img" aria-label="Fine line sketch of a hillside vineyard with a farmhouse and cypress trees"></div>

    <div class="seal" aria-hidden="true"></div>
    <span class="seal-name">Vrbolanec</span>

    <p class="varietal">Sauvignon Blanc</p>
    <div class="rule"></div>
    <p class="origin">Croatia</p>
  </main>
</body>
</html>
```